Tobin Quartz Portal Page . It's guarantee project!

We need a clean and professional modern web application portal page
That includes the Login & Application Selection screen

Also, I need to design both Desktop and Mobile sizes.
We have an example design for our target

The application is Jetty Schedule and related data.
Our client is a bit conservative.

Theme color preferred : #00508B (main) #DF0D83 (secondary)

Target Market(s)

Oil & Fuel & Gasoline

Number of Pages Required

2 page

Font styles to use
Sans Serif

Colors
0054AA
0677BA
7BADD7
CADEEF
E8F1F8
E54698
E96AAD
F1A4CE
F9D9EA
FCEFF6

Requirements
Must have
• Login Page & Main Screen

```html
<!DOCTYPE html>
<html lang="en">
<head>
<meta charset="utf-8">
<title>Jetty Connect Portal – Sign In and Application Selection</title>
<link rel="stylesheet" href="https://fonts.googleapis.com/css2?family=Inter:wght@400;500;600&family=Roboto:wght@400;500;700&display=swap">
<style>
  :root {
    --board: #f0ebeb;
    --surface: #ffffff;
    --frame-line: #dcd6d6;
    --primary: #00508b;
    --secondary: #df0d83;
    --header-light: #dfeff8;
    --on-primary: #ffffff;
    --card-shadow: rgba(0, 80, 139, 0.10);
    --illus-lavender: #e4e2fb;
    --illus-blue: #4c9bd8;
    --illus-blue-light: #9cc8ec;
    --illus-pink: #e96aad;
    --illus-pink-soft: #f9d9ea;
  }

  * { box-sizing: border-box; margin: 0; padding: 0; }

  html, body {
    width: 1200px;
    height: 922px;
    overflow: hidden;
    background: var(--board);
    font-family: "Inter", Arial, sans-serif;
    color: var(--primary);
  }

  .board { position: relative; width: 1200px; height: 922px; }

  .frame-label {
    position: absolute;
    font-size: 10px;
    font-weight: 400;
    color: var(--primary);
    line-height: 12px;
  }

  .frame {
    position: absolute;
    background: var(--surface);
    border: 1px solid var(--frame-line);
    overflow: hidden;
  }

  /* ---------- Sign-in screen ---------- */
  .login-header {
    position: absolute;
    left: 0; top: 0; right: 0;
    height: 31px;
    background: var(--header-light);
  }

  .brand {
    position: absolute;
    top: 0;
    height: 31px;
    display: flex;
    align-items: center;
    gap: 3px;
    font-family: "Roboto", Arial, sans-serif;
    font-size: 8px;
    font-weight: 500;
    color: var(--primary);
  }
  .brand-dot {
    width: 9px; height: 9px;
    border-radius: 50%;
    background: var(--secondary);
  }

  .signin-form {
    position: absolute;
    top: 60px;
    font-family: "Roboto", Arial, sans-serif;
  }
  .signin-title {
    position: absolute;
    left: 0; right: 0; top: 0;
    line-height: 14px;
    text-align: center;
    font-size: 9.5px;
    font-weight: 500;
    color: var(--primary);
  }
  .field {
    position: absolute;
    left: 0; right: 0;
    height: 21px;
    border: 0.8px solid var(--primary);
    border-radius: 2px;
  }
  .field-email { top: 29px; }
  .field-password { top: 63px; }
  .field-label {
    position: absolute;
    left: 5px; top: -4px;
    padding: 0 1.5px;
    background: var(--surface);
    font-size: 5px;
    line-height: 7px;
    color: var(--primary);
  }
  .field-toggle {
    position: absolute;
    right: 7px; top: 5.5px;
    width: 9px; height: 9px;
  }
  .btn-signin {
    position: absolute;
    left: 0; right: 0; top: 105px;
    height: 21px;
    border: none;
    border-radius: 1.5px;
    background: var(--secondary);
    color: var(--on-primary);
    font-family: "Roboto", Arial, sans-serif;
    font-size: 5.5px;
    font-weight: 400;
    letter-spacing: 0.1px;
    display: flex;
    align-items: center;
    justify-content: center;
  }

  /* ---------- Application selection screen ---------- */
  .app-header {
    position: absolute;
    left: 0; top: 0; right: 0;
    height: 31px;
    background: var(--primary);
    color: var(--on-primary);
  }
  .nav-home {
    position: absolute;
    top: 0; height: 31px;
    display: flex;
    align-items: center;
    gap: 2px;
    font-size: 6.3px;
  }
  .nav-home svg { width: 6px; height: 6px; }
  .user {
    position: absolute;
    top: 8px;
    line-height: 7.5px;
  }
  .user-name { font-size: 6.3px; font-weight: 600; }
  .user-email { font-size: 5.3px; font-weight: 400; }
  .user-avatar {
    position: absolute;
    top: 8px;
    width: 15px; height: 15px;
  }

  .app-card {
    position: absolute;
    background: var(--surface);
    border-radius: 8px;
    box-shadow: 0 0 5px var(--card-shadow);
  }
  .app-illustration {
    position: absolute;
    left: 50%;
    transform: translateX(-50%);
    border-radius: 45% 50% 42% 48%;
  }
  .illus-planning {
    background: radial-gradient(circle at 55% 45%, var(--illus-lavender) 0 45%, var(--illus-blue-light) 60%, var(--illus-pink-soft) 100%);
  }
  .illus-tracking {
    background: linear-gradient(135deg, var(--illus-blue) 0%, var(--illus-blue-light) 55%, var(--illus-pink) 100%);
    border-radius: 8px 40% 10px 30%;
  }
  .illus-performance {
    background: radial-gradient(circle at 50% 70%, var(--illus-blue) 0 50%, var(--illus-lavender) 70%, var(--illus-pink-soft) 100%);
  }
  .app-name {
    position: absolute;
    left: 0; right: 0;
    text-align: center;
    font-weight: 600;
    color: var(--primary);
    white-space: nowrap;
  }

  .app-card--desktop { width: 142px; height: 142px; }
  .app-card--desktop .app-illustration { top: 15px; width: 101px; height: 93px; }
  .app-card--desktop .app-name { top: 117px; line-height: 14px; font-size: 8.5px; }

  .app-card--tablet { width: 84px; height: 84px; }
  .app-card--tablet .app-illustration { top: 9px; width: 62px; height: 56px; }
  .app-card--tablet .app-name { top: 70px; line-height: 10px; font-size: 6.3px; }

  .app-card--mobile { width: 62px; height: 62px; border-radius: 6px; }
  .app-card--mobile .app-illustration { top: 8px; width: 44px; height: 40px; }
  .app-card--mobile .app-name { top: 50px; line-height: 8px; font-size: 4.5px; }
</style>
</head>
<body>
<main class="board">

  <!-- Sign in: desktop -->
  <p class="frame-label" style="left:15px; top:18px;">Desktop 1440</p>
  <section class="frame" style="left:15px; top:39px; width:561px; height:399px;">
    <header class="login-header">
      <div class="brand" style="left:59px;"><span class="brand-dot"></span>Jetty Connect</div>
    </header>
    <form class="signin-form" style="left:210px; width:140px;">
      <h1 class="signin-title">SIGN IN</h1>
      <div class="field field-email"><span class="field-label">Email</span></div>
      <div class="field field-password"><span class="field-label">Password</span>
        <svg class="field-toggle" viewBox="0 0 24 24" fill="none" stroke="#00508b" stroke-width="2.4" stroke-linecap="round"><path d="M2 12s3.5-6 10-6 10 6 10 6-3.5 6-10 6S2 12 2 12z"/><circle cx="12" cy="12" r="3"/><path d="M4 20L20 4"/></svg>
      </div>
      <div class="btn-signin">SIGN IN</div>
    </form>
  </section>

  <!-- Applications: desktop -->
  <p class="frame-label" style="left:616px; top:18px;">Desktop 1440</p>
  <section class="frame" style="left:616px; top:39px; width:561px; height:399px;">
    <header class="app-header">
      <div class="nav-home" style="left:58px;">
        <svg viewBox="0 0 24 24" fill="none" stroke="#fff" stroke-width="2.2"><path d="M3 11l9-8 9 8v10h-6v-6H9v6H3z"/></svg>Home
      </div>
      <div class="user" style="left:420px;">
        <div class="user-name">Mara Lind</div>
        <div class="user-email">mara.lind@example.com</div>
      </div>
      <svg class="user-avatar" style="left:487px;" viewBox="0 0 24 24"><circle cx="12" cy="12" r="12" fill="#fff"/><circle cx="12" cy="9" r="4" fill="#00508b"/><path d="M5 19c1.5-3.5 4-5 7-5s5.5 1.5 7 5" fill="#00508b"/></svg>
    </header>
    <article class="app-card app-card--desktop" style="left:58px; top:56px;">
      <div class="app-illustration illus-planning" role="img" aria-label="Illustration of a clock, calendar, checklist and envelope for planning"></div>
      <h2 class="app-name">Jetty Planning</h2>
    </article>
    <article class="app-card app-card--desktop" style="left:209px; top:56px;">
      <div class="app-illustration illus-tracking" role="img" aria-label="Illustration of a route map with location pins, a ship and a phone for tracking"></div>
      <h2 class="app-name">Jetty Tracking</h2>
    </article>
    <article class="app-card app-card--desktop" style="left:360px; top:56px;">
      <div class="app-illustration illus-performance" role="img" aria-label="Illustration of an offshore rig, tankers and a target for port performance"></div>
      <h2 class="app-name">Jetty/Port Perfomance</h2>
    </article>
  </section>

  <!-- Sign in: tablet -->
  <p class="frame-label" style="left:15px; top:486px;">Tablet 768</p>
  <section class="frame" style="left:15px; top:507px; width:299px; height:398px;">
    <header class="login-header">
      <div class="brand" style="left:12px;"><span class="brand-dot"></span>Jetty Connect</div>
    </header>
    <form class="signin-form" style="left:80px; width:140px;">
      <h1 class="signin-title">SIGN IN</h1>
      <div class="field field-email"><span class="field-label">Email</span></div>
      <div class="field field-password"><span class="field-label">Password</span>
        <svg class="field-toggle" viewBox="0 0 24 24" fill="none" stroke="#00508b" stroke-width="2.4" stroke-linecap="round"><path d="M2 12s3.5-6 10-6 10 6 10 6-3.5 6-10 6S2 12 2 12z"/><circle cx="12" cy="12" r="3"/><path d="M4 20L20 4"/></svg>
      </div>
      <div class="btn-signin">SIGN IN</div>
    </form>
  </section>

  <!-- Sign in: mobile -->
  <p class="frame-label" style="left:339px; top:486px;">Mobile 375</p>
  <section class="frame" style="left:339px; top:507px; width:147px; height:261px;">
    <header class="login-header">
      <div class="brand" style="left:7px;"><span class="brand-dot"></span>Jetty Connect</div>
    </header>
    <form class="signin-form" style="left:6px; width:134px;">
      <h1 class="signin-title">SIGN IN</h1>
      <div class="field field-email"><span class="field-label">Email</span></div>
      <div class="field field-password"><span class="field-label">Password</span>
        <svg class="field-toggle" viewBox="0 0 24 24" fill="none" stroke="#00508b" stroke-width="2.4" stroke-linecap="round"><path d="M2 12s3.5-6 10-6 10 6 10 6-3.5 6-10 6S2 12 2 12z"/><circle cx="12" cy="12" r="3"/><path d="M4 20L20 4"/></svg>
      </div>
      <div class="btn-signin">SIGN IN</div>
    </form>
  </section>

  <!-- Applications: tablet -->
  <p class="frame-label" style="left:616px; top:486px;">Tablet 768</p>
  <section class="frame" style="left:616px; top:507px; width:299px; height:398px;">
    <header class="app-header">
      <div class="nav-home" style="left:12px;">
        <svg viewBox="0 0 24 24" fill="none" stroke="#fff" stroke-width="2.2"><path d="M3 11l9-8 9 8v10h-6v-6H9v6H3z"/></svg>Home
      </div>
      <div class="user" style="left:204px;">
        <div class="user-name">Mara Lind</div>
        <div class="user-email">mara.lind@example.com</div>
      </div>
      <svg class="user-avatar" style="left:271px;" viewBox="0 0 24 24"><circle cx="12" cy="12" r="12" fill="#fff"/><circle cx="12" cy="9" r="4" fill="#00508b"/><path d="M5 19c1.5-3.5 4-5 7-5s5.5 1.5 7 5" fill="#00508b"/></svg>
    </header>
    <article class="app-card app-card--tablet" style="left:14px; top:56px;">
      <div class="app-illustration illus-planning" role="img" aria-label="Illustration of a clock, calendar, checklist and envelope for planning"></div>
      <h2 class="app-name">Jetty Planning</h2>
    </article>
    <article class="app-card app-card--tablet" style="left:107px; top:56px;">
      <div class="app-illustration illus-tracking" role="img" aria-label="Illustration of a route map with location pins, a ship and a phone for tracking"></div>
      <h2 class="app-name">Jetty Tracking</h2>
    </article>
    <article class="app-card app-card--tablet" style="left:201px; top:56px;">
      <div class="app-illustration illus-performance" role="img" aria-label="Illustration of an offshore rig, tankers and a target for port performance"></div>
      <h2 class="app-name">Jetty/Port Perfomance</h2>
    </article>
  </section>

  <!-- Applications: mobile -->
  <p class="frame-label" style="left:940px; top:486px;">Mobile 375</p>
  <section class="frame" style="left:940px; top:507px; width:146px; height:261px;">
    <header class="app-header">
      <div class="nav-home" style="left:7px;">
        <svg viewBox="0 0 24 24" fill="none" stroke="#fff" stroke-width="2.2"><path d="M3 11l9-8 9 8v10h-6v-6H9v6H3z"/></svg>Home
      </div>
      <div class="user" style="left:58px;">
        <div class="user-name">Mara Lind</div>
        <div class="user-email">mara.lind@example.com</div>
      </div>
      <svg class="user-avatar" style="left:124px;" viewBox="0 0 24 24"><circle cx="12" cy="12" r="12" fill="#fff"/><circle cx="12" cy="9" r="4" fill="#00508b"/><path d="M5 19c1.5-3.5 4-5 7-5s5.5 1.5 7 5" fill="#00508b"/></svg>
    </header>
    <article class="app-card app-card--mobile" style="left:6px; top:43px;">
      <div class="app-illustration illus-planning" role="img" aria-label="Illustration of a clock, calendar, checklist and envelope for planning"></div>
      <h2 class="app-name">Jetty Planning</h2>
    </article>
    <article class="app-card app-card--mobile" style="left:77px; top:43px;">
      <div class="app-illustration illus-tracking" role="img" aria-label="Illustration of a route map with location pins, a ship and a phone for tracking"></div>
      <h2 class="app-name">Jetty Tracking</h2>
    </article>
    <article class="app-card app-card--mobile" style="left:6px; top:114px;">
      <div class="app-illustration illus-performance" role="img" aria-label="Illustration of an offshore rig, tankers and a target for port performance"></div>
      <h2 class="app-name">Jetty/Port Perfomance</h2>
    </article>
  </section>

</main>
</body>
</html>
```